mailer to distressed properties

Our business is a company that buys houses for cash that are in need of repairs. Need to create a post card to mail to homeowners to get them to call us to give them a price on their home for cash and purchase it. Would like a run down house on background and our company info so they could call us. Have a logo would like to incorporate in it. Want to get to the point across we can buy there home for cash on any condition and close quickly. We can also buy them if they have permit or violation issues. We also buy homes going into foreclosure so we can stop foreclosure. Company name is R & T Dwellings. P o box 829 Westmere my 11947. 631-482-9163. Email us at info@randtdwellings.example and our website Randtdwellings.example. Open to a lot of direct designs excited to see what you come up with. Anything else you can think we are open to see it. Email us with any other questions . Also can add fast closing and save no real estate commissions collected. We want it in color your choice. Also on font open to anything and size of font.

Target Market(s)

Run down and distressed properties

Industry/Entity Type

Construction Company

Font styles to use
Serif
Sans Serif

Requirements
Must have
• A background of a distressed home and our info how to call us
Nice to have
• Colorful and attractive
Should not have
• Nothing I can think of

```html
<!DOCTYPE html>
<html lang="en">
<head>
<meta charset="utf-8">
<title>R &amp; T Dwellings – Cash Home Buyer Postcard</title>
<link href="https://fonts.googleapis.com/css2?family=Oswald:wght@400;500;600;700&family=Roboto:wght@400;500;700;900&family=Roboto+Condensed:wght@400;700&display=swap" rel="stylesheet">
<style>
  :root {
    --red: #e2161d;
    --navy: #1e2c48;
    --black: #111214;
    --white: #ffffff;
    --paper: #f4f4f4;
    --grey: #d9d9d9;
    --ink: #1a1a1a;
    --badge: #161616;
  }
  html, body {
    margin: 0; padding: 0;
    width: 1200px; height: 1000px;
    overflow: hidden;
    background: #e9e9e9;
  }
  .postcard {
    position: absolute;
    left: 49px; top: 146px;
    width: 1102px; height: 708px;
    background: var(--black);
    overflow: hidden;
    font-family: "Roboto", Arial, sans-serif;
    box-shadow: 0 6px 18px rgba(0,0,0,.25);
  }
  .shapes { position: absolute; inset: 0; }

  /* left panel */
  .brand {
    position: absolute; left: 0; top: 112px; width: 311px;
    text-align: center;
    font-family: "Roboto", Arial, sans-serif;
    font-weight: 900; font-size: 34px; color: var(--black);
    letter-spacing: .2px;
  }
  .brand-mark {
    position: absolute; left: 133px; top: 48px;
    width: 46px; height: 46px; background: var(--black);
  }
  .pitch {
    position: absolute; left: 36px; top: 206px; width: 270px;
    font-family: "Oswald", "Roboto Condensed", sans-serif;
    font-weight: 600; font-size: 28px; line-height: 37px;
    color: var(--black); text-transform: uppercase;
  }
  .pitch .lead { font-size: 34px; }
  .pitch em { font-style: normal; color: var(--red); }

  .call-now {
    position: absolute; left: 76px; top: 560px; width: 235px;
    text-align: center; color: var(--white);
    font-family: "Oswald", "Roboto Condensed", sans-serif; font-weight: 600;
  }
  .call-now .phone-icon { display: block; margin: 0 auto 6px; }
  .call-now .label { font-size: 40px; line-height: 44px; }
  .call-now .number { font-size: 36px; line-height: 48px; letter-spacing: .3px; }

  /* headline */
  .headline {
    position: absolute; left: 311px; top: 36px; width: 773px; height: 61px;
    display: flex; align-items: center; justify-content: center;
    font-family: "Oswald", "Roboto Condensed", sans-serif;
    font-weight: 600; font-size: 40px; color: var(--white);
    text-transform: uppercase; letter-spacing: .3px;
  }
  .headline em { font-style: normal; color: var(--red); margin: 0 10px; }
  .subhead {
    position: absolute; left: 311px; top: 98px; width: 773px;
    text-align: center;
    font-family: "Oswald", "Roboto Condensed", sans-serif;
    font-weight: 500; font-size: 23px; color: var(--white);
    text-transform: uppercase;
    text-shadow: 0 1px 3px rgba(0,0,0,.6);
  }

  /* badge */
  .hours-badge {
    position: absolute; left: 885px; top: 371px;
    width: 168px; height: 168px; border-radius: 50%;
    background: var(--badge); border: 5px solid var(--white);
    box-sizing: border-box;
    display: flex; flex-direction: column; align-items: center; justify-content: center;
    font-family: "Oswald", "Roboto Condensed", sans-serif; font-weight: 500;
    color: var(--white); text-transform: uppercase; text-align: center;
    font-size: 17px; line-height: 21px;
  }
  .hours-badge .big { font-size: 24px; line-height: 28px; color: var(--red); font-weight: 600; }
  .hours-badge em { font-style: normal; color: var(--red); }

  /* why choose */
  .why-title {
    position: absolute; left: 352px; top: 504px; width: 296px; height: 40px;
    background: var(--red); color: var(--white);
    display: flex; align-items: center; justify-content: center;
    font-family: "Roboto Condensed", Arial, sans-serif; font-weight: 700; font-size: 22px;
    box-shadow: 0 2px 3px rgba(0,0,0,.3);
  }
  .benefits {
    position: absolute; left: 326px; top: 568px; width: 352px; height: 104px;
    display: flex;
  }
  .benefit {
    flex: 1; text-align: center;
    border-right: 1px solid #b9b9b9;
    font-family: "Roboto Condensed", Arial, sans-serif; font-size: 15px; line-height: 19px;
    color: var(--ink);
  }
  .benefit:last-child { border-right: 0; }
  .benefit svg { display: block; margin: 4px auto 10px; }

  /* contact */
  .contact {
    position: absolute; left: 826px; top: 722px;
  }
  .contact-block {
    position: absolute; left: 720px; top: 518px; width: 350px;
    font-family: "Roboto", Arial, sans-serif; color: var(--ink);
  }
  .contact-block h2 {
    margin: 0 0 10px; font-size: 23px; font-weight: 700;
  }
  .contact-line {
    display: flex; align-items: center; gap: 8px;
    font-size: 18px; line-height: 24px;
  }
  .contact-line svg { flex: none; }
</style>
</head>
<body>
<div class="postcard">
  <svg class="shapes" width="1102" height="708" viewBox="0 0 1102 708" aria-hidden="false">
    <defs>
      <linearGradient id="panelFade" x1="0" y1="0" x2="0" y2="1">
        <stop offset="0" stop-color="#ffffff"/>
        <stop offset="1" stop-color="#e4e4e4"/>
      </linearGradient>
      <linearGradient id="houseScene" x1="0" y1="0" x2="0" y2="1">
        <stop offset="0" stop-color="#7fb3e3"/>
        <stop offset=".3" stop-color="#c9d4dc"/>
        <stop offset=".55" stop-color="#b9bcbf"/>
        <stop offset=".8" stop-color="#8e9a78"/>
        <stop offset="1" stop-color="#5f7a3c"/>
      </linearGradient>
      <linearGradient id="grass" x1="0" y1="0" x2="0" y2="1">
        <stop offset="0" stop-color="#a8b59a"/>
        <stop offset="1" stop-color="#4f6d2e"/>
      </linearGradient>
      <linearGradient id="strip" x1="0" y1="0" x2="0" y2="1">
        <stop offset="0" stop-color="#ffffff"/>
        <stop offset="1" stop-color="#d8d8d8"/>
      </linearGradient>
    </defs>
    <!-- left panel -->
    <rect x="0" y="0" width="311" height="688" fill="url(#panelFade)"/>
    <polygon points="0,563 311,330 311,688 0,688" fill="url(#grass)" role="img" aria-label="Overgrown grass in front of a run-down house"/>
    <line x1="60" y1="186" x2="250" y2="186" stroke="#c4c4c4" stroke-width="2"/>
    <polygon points="311,367 76,529 76,688 311,688" fill="var(--red)"/>
    <!-- main photo -->
    <rect x="311" y="19" width="773" height="483" fill="url(#houseScene)" role="img" aria-label="Photo of a distressed, abandoned two-storey house with broken roof and overgrown yard"/>
    <rect x="311" y="36" width="773" height="61" fill="var(--navy)" opacity=".88"/>
    <!-- bottom strip -->
    <rect x="311" y="502" width="380" height="186" fill="url(#strip)"/>
    <rect x="700" y="502" width="384" height="186" fill="url(#strip)"/>
  </svg>

  <div class="brand-mark"></div>
  <div class="brand">R &amp; T Dwellings</div>

  <p class="pitch" style="margin:0">
    <span class="lead"><em>Call us</em> &amp; get</span><br>
    a price on your<br>
    <em>home</em> for cash and<br>
    <em>purchase</em> it.
  </p>

  <div class="call-now">
    <svg class="phone-icon" width="46" height="46" viewBox="0 0 46 46">
      <circle cx="23" cy="23" r="20" fill="none" stroke="#fff" stroke-width="3"/>
      <path d="M16 13c1-1 2.5-1 3.3.2l2 3c.6.9.4 2-.4 2.7l-1.4 1.1c1 2.4 2.9 4.4 5.4 5.5l1.1-1.4c.7-.8 1.9-1 2.7-.4l3 2c1.2.8 1.2 2.4.2 3.3l-1.5 1.4c-1.4 1.3-3.5 1.6-5.3.8-5-2.3-8.8-6.1-11-11-.8-1.8-.5-3.9.8-5.3z" fill="#fff"/>
    </svg>
    <div class="label">CALL NOW</div>
    <div class="number">631-482-9163</div>
  </div>

  <div class="headline">Quickly<em>Sell</em>your house<em>fast</em>for cash</div>
  <div class="subhead">Fast closing and save no real estate commissions collected</div>

  <div class="hours-badge">
    <span class="big">Feel free</span>
    <span>to contact us</span>
    <span><em>24 hours</em> a day</span>
    <span><em>7 days</em></span>
    <span>a week!</span>
  </div>

  <div class="why-title">Why to Choose R&amp;Tdwellings?</div>
  <div class="benefits">
    <div class="benefit">
      <svg width="30" height="32" viewBox="0 0 30 32"><path d="M15 2 L27 6 V15 C27 23 21 28 15 30 C9 28 3 23 3 15 V6 Z" fill="none" stroke="var(--red)" stroke-width="3"/><path d="M9 16 L13.5 20.5 L21 12" fill="none" stroke="var(--red)" stroke-width="3"/></svg>
      Trusted<br>Professionals
    </div>
    <div class="benefit">
      <svg width="30" height="32" viewBox="0 0 30 32"><text x="15" y="28" text-anchor="middle" font-family="Roboto, sans-serif" font-weight="700" font-size="32" fill="var(--red)">$</text></svg>
      Get the Best<br>Cash Offer
    </div>
    <div class="benefit">
      <svg width="32" height="32" viewBox="0 0 32 32"><polygon points="16,1 20,12 31,12 22,19 25.5,30.5 16,23.5 6.5,30.5 10,19 1,12 12,12" fill="var(--red)"/></svg>
      Very Fast<br>Process
    </div>
    <div class="benefit">
      <svg width="34" height="32" viewBox="0 0 34 32"><polygon points="17,1 33,15 29,15 29,31 21,31 21,21 13,21 13,31 5,31 5,15 1,15" fill="var(--red)"/></svg>
      Licensed<br>and Insured
    </div>
  </div>

  <div class="contact-block">
    <h2>R &amp; T Dwellings.</h2>
    <div class="contact-line">
      <svg width="14" height="18" viewBox="0 0 14 18"><path d="M7 1C3.7 1 1 3.6 1 6.9 1 11 7 17 7 17s6-6 6-10.1C13 3.6 10.3 1 7 1z" fill="var(--red)"/><circle cx="7" cy="7" r="2.3" fill="#fff"/></svg>
      P.O. Box 829, Westmere NY 11947
    </div>
    <div class="contact-line">
      <svg width="16" height="16" viewBox="0 0 16 16"><circle cx="8" cy="8" r="7" fill="none" stroke="var(--red)" stroke-width="1.6"/><path d="M5.4 4.3c.4-.4 1-.4 1.3.1l.8 1.2c.2.4.2.8-.2 1.1l-.5.4c.4 1 1.2 1.8 2.2 2.2l.4-.5c.3-.4.7-.4 1.1-.2l1.2.8c.5.3.5 1 .1 1.3l-.6.6c-.6.5-1.4.6-2.1.3-2-.9-3.5-2.5-4.4-4.4-.3-.7-.2-1.5.3-2.1z" fill="var(--red)"/></svg>
      631-482-9163.
    </div>
    <div class="contact-line">
      <svg width="16" height="12" viewBox="0 0 16 12"><rect x="1" y="1" width="14" height="10" fill="none" stroke="var(--red)" stroke-width="1.6"/><path d="M1 1 L8 7 L15 1" fill="none" stroke="var(--red)" stroke-width="1.6"/></svg>
      info@randtdwellings.example
    </div>
    <div class="contact-line">
      <svg width="16" height="16" viewBox="0 0 16 16"><circle cx="8" cy="8" r="7" fill="none" stroke="var(--red)" stroke-width="1.6"/><ellipse cx="8" cy="8" rx="3" ry="7" fill="none" stroke="var(--red)" stroke-width="1.3"/><line x1="1" y1="8" x2="15" y2="8" stroke="var(--red)" stroke-width="1.3"/></svg>
      www.Randtdwellings.example.
    </div>
  </div>
</div>
</body>
</html>
```